Brightmoor Fire Solutions business card, logo and web design.

We need business cards for our new company. We are based in South Africa. We specialise in fire detection, fire prevention, security, access control and CCTV in buildings. We service and install sprinkler systems, fire hose reals and fire extinguishers in buildings. Our slogan in the company is "Compliance is our business" . We strive to be innovators in our field and deliver the best service possible at the best quality. We want to be the best in our field. We don't have any colour preferences as long as it relates to our type of business.
Our target market is clients that owns big buildings with multiple levels, such a malls,office buildings or warehouses.

Target Market(s)

Industry/Entity Type

Fire Safety

Contact Information for Business Card

The front of the card should have the company name (Brightmoor Fire Solutions (PTY) LTD. and a description of the company. Fire engineering & security services.

Logo Text

Compliance is our business

Number of Pages Required

4 page

Font styles to use
Serif

Colors

Designer to choose colors to be used in the design.

Requirements
Must have
• The company name, the logo and all the details on the back of the card. It should be simple and not to busy.
Nice to have
• Just something different and new. Brightmoor means - innovate so the card should represent our name.
Should not have
• Small pictures or lots of graphics on.

```html
<!DOCTYPE html>
<html lang="en">
<head>
<meta charset="utf-8">
<title>Brightmoor Fire Solutions – Business Card</title>
<link rel="stylesheet" href="https://fonts.googleapis.com/css2?family=Lato:wght@400&family=Oswald:wght@400&display=swap">
<style>
  :root {
    --backdrop: #4a4a4a;
    --card: #ffffff;
    --accent: #f26b21;
    --ink: #6b6b6b;
    --ink-soft: #7a7a7a;
  }
  * { margin: 0; padding: 0; box-sizing: border-box; }
  html, body {
    width: 1200px; height: 1000px; overflow: hidden;
    background: var(--backdrop);
  }
  .stage { position: relative; width: 1200px; height: 1000px; }
  .card {
    position: absolute; left: 269px; width: 662px; height: 378px;
    background: var(--card);
    box-shadow: 0 4px 14px rgba(0,0,0,0.35);
  }
  .card--front { top: 108px; }
  .card--back { top: 521px; height: 379px; }

  .edge-rule {
    position: absolute; left: 151px; width: 360px; height: 2px;
    background: var(--accent);
  }
  .edge-rule--top { top: 0; }
  .edge-rule--bottom { bottom: 0; }

  .company {
    position: absolute; left: 0; right: 0; top: 140px;
    text-align: center;
    font-family: "Lato", sans-serif;
    font-weight: 400;
  }
  .company__name {
    display: block;
    color: var(--accent);
    font-size: 52px; line-height: 60px;
    letter-spacing: 1px;
  }
  .company__legal {
    display: block;
    margin-top: 14px;
    color: var(--ink);
    font-size: 20px; letter-spacing: 1px;
  }
  .tagline {
    position: absolute; left: 0; right: 0; top: 318px;
    text-align: center;
    font-family: "Lato", sans-serif;
    font-size: 17.5px; color: var(--ink);
  }

  .contact { position: absolute; left: 44px; right: 44px; top: 130px;
    font-family: "Lato", sans-serif; color: var(--ink); }
  .contact__name {
    font-family: "Oswald", sans-serif; font-weight: 400; font-size: 25px;
    color: var(--accent); line-height: 34px; letter-spacing: 0.3px;
  }
  .contact__role { font-size: 15px; margin-top: 2px; }
  .contact__mark { width: 32px; height: 2px; background: var(--accent); margin-top: 10px; }
  .contact__address { font-size: 15.5px; margin-top: 30px; letter-spacing: 0.2px; word-spacing: 1px; }
  .contact__rule { height: 1px; background: var(--accent); }
  .contact__rule--upper { margin-top: 14px; }
  .contact__lines {
    display: flex; justify-content: space-between; align-items: center;
    font-size: 15px; color: var(--ink-soft); height: 43px;
  }
  .contact__item { display: flex; align-items: center; gap: 4px; }
  .contact__item svg { width: 12px; height: 12px; fill: #333; }
  .contact__legal { font-size: 15px; margin-top: 17px; color: var(--ink-soft); }
</style>
</head>
<body>
<main class="stage">
  <section class="card card--front" aria-label="Card front">
    <span class="edge-rule edge-rule--top"></span>
    <div class="company">
      <span class="company__name">BRIGHTMOOR</span>
      <span class="company__legal">FIRE SOLUTIONS (PTY) LTD</span>
    </div>
    <p class="tagline">FIRE ENGINEERING &amp; SECURITY SERVICES</p>
    <span class="edge-rule edge-rule--bottom"></span>
  </section>

  <section class="card card--back" aria-label="Card back">
    <div class="contact">
      <h1 class="contact__name">PIETER VENTER</h1>
      <p class="contact__role">MANAGING DIRECTOR</p>
      <div class="contact__mark"></div>
      <p class="contact__address">14 PROTEA AVENUE &nbsp;.&nbsp; LYNNWOOD &nbsp;.&nbsp; PRETORIA &nbsp;.&nbsp; 0081 &nbsp;.&nbsp; SOUTH AFRICA</p>
      <div class="contact__rule contact__rule--upper"></div>
      <div class="contact__lines">
        <span class="contact__item">
          <svg viewBox="0 0 12 12" aria-hidden="true"><path d="M2.5 1 L4.5 1 L5 3.5 L3.8 4.5 C4.5 6 6 7.5 7.5 8.2 L8.5 7 L11 7.5 L11 9.5 C11 10.3 10.3 11 9.5 11 C5 10.7 1.3 7 1 2.5 C1 1.7 1.7 1 2.5 1Z"/></svg>
          012-555-0182
        </span>
        <span class="contact__item">
          <svg viewBox="0 0 12 12" aria-hidden="true"><path d="M3 0.5 H9 V11.5 H3 Z M4 1.5 V9.5 H8 V1.5 Z M5.5 10 H6.5 V11 H5.5 Z"/></svg>
          082-555-0164
        </span>
        <span class="contact__item">
          <svg viewBox="0 0 12 12" aria-hidden="true"><path d="M3 1 H9 V4 H3 Z M1 4.5 H11 V9 H9 V7 H3 V9 H1 Z M3.5 7.5 H8.5 V11 H3.5 Z"/></svg>
          012-555-0147
        </span>
        <span class="contact__item">
          <svg viewBox="0 0 12 12" aria-hidden="true"><path d="M1 2.5 H11 V9.5 H1 Z M1.5 3 L6 6.5 L10.5 3 V3.6 L6 7.2 L1.5 3.6 Z" fill-rule="evenodd"/></svg>
          info@brightmoor.co.za
        </span>
      </div>
      <div class="contact__rule"></div>
      <p class="contact__legal">VAT NO: 4730158826 &nbsp;.&nbsp; REG NO: 2019/482317/07</p>
    </div>
  </section>
</main>
</body>
</html>
```